Float and wellness centre needs a website refresh

Our float and wellness centre has been operating in Brisbane, Australia for 3 months. Our website is functional and easy to use, but it lacks a compelling visual experience that sells our awesome services to our customers.<br/><br/>We would like a complete redesign of our webpage. It is very important that the redesign considers the page layout for mobile users and the winning design will need to show both a desktop and mobile version of each of the pages listed below.<br/><br/>Out current website can be found at https://www.ebbtidehaven.com.au/<br/><br/>The winning design will need to provide proposals for redesigning the 4 pages listed below:<br/>Home Page - https://www.ebbtidehaven.com.au/<br/>Float Page - https://www.ebbtidehaven.com.au/services/float<br/>Build Gift Card page - https://www.ebbtidehaven.com.au/giftcard/stepone?location=kelsworth<br/>Booking Page - https://www.ebbtidehaven.com.au/Calendar/Day?centerId=kelsworth&selectedCategory=FLOAT&date=12/18/2019%2000:00:00%20+10:00&sessionLength=60<br/><br/>We only need the 4 pages listed above as our web developer will use the assets from the above pages to standardize all the other pages in the site. It is very important your proposed pages contain the same information as our current pages so that we can properly see the complete layout.<br/><br/>The Home page must display the business logo in some way. We would like the website to have a white background and for it make tasteful use of color to highlight key features on the pages. Where color is used it should harmonize with the business logo. The website needs to feel bright, simple and relaxing. Our current site does not use images very well and we have had professional photos taken of the center and the float rooms specifically for this website project. You can download these, and the business logo images here: http://ebbtidehaven.com.au/websiteimages.zip <br/><br/>We have included a few links below to other centers who have pages that we like: <br/><br/>https://www.drifthollowpods.com/ <br/>https://www.quietnook.com.au/ <br/>https://www.moonbaysoak.com.au/<br/>

Industry/Entity Type

Health And Wellness

Number of Pages Required

4 page

Font styles to use
Sans Serif

Colors

Designer to choose colors to be used in the design.

Requirements
Must have
• It is very important your proposed pages contain the same information as our current pages so that we can properly see the complete layout.
• The Home page must display the business logo in some way.
• Where color is used it should harmonize with the business logo.
Nice to have
• The website needs to feel bright, simple and relaxing. Our current site does not use images very well and we have had professional photos taken of the center and the float rooms specifically for this website project. You can download these, and the business logo images here: http://ebbtidehaven.com.au/websiteimages.zip
Should not have
• Dark pages.

```html
<!DOCTYPE html>
<html lang="en">
<head>
<meta charset="utf-8">
<title>Ebbtide Haven — Home</title>
<link href="https://fonts.googleapis.com/css2?family=Open+Sans:wght@600;700;800&family=Source+Sans+3:wght@400;600;700&display=swap" rel="stylesheet">
<style>
:root{
  --plum:#a0578a;
  --plum-dark:#7d3f6b;
  --rose:#c06a9a;
  --blush:#f4eaf0;
  --blush-soft:#f8f2f6;
  --paper:#fcf9fb;
  --ink:#3a2f37;
  --ink-soft:#5d535a;
  --white:#ffffff;
  --accent-blue:#5b7ec8;
}
*{box-sizing:border-box;margin:0;padding:0}
html,body{width:1200px;height:1200px;overflow:hidden;background:#fbf8fa}
body{font-family:"Source Sans 3",sans-serif;color:var(--ink)}
.stage{position:absolute;left:0;top:0;width:1932px;height:1932px;transform:scale(.62112);transform-origin:0 0}
.page{position:absolute;left:651px;top:20px;width:551px;height:1863px;background:var(--paper);overflow:hidden}
.abs{position:absolute}
/* hero */
.hero-shape{position:absolute;left:0;top:0}
.brand-mark{left:12px;top:30px;width:34px;text-align:center;color:var(--white);font-size:6px;font-weight:700;line-height:1.1}
.brand-mark .dot{display:block;width:14px;height:14px;border-radius:50%;background:var(--rose);margin:0 auto 3px}
.nav{top:13px;font-size:8px;color:var(--white);font-weight:600}
.nav a{position:absolute;color:inherit;text-decoration:none;white-space:nowrap}
.nav a.is-active{color:var(--rose)}
.hero-title{left:104px;top:64px;font-family:"Open Sans",sans-serif;font-weight:600;font-size:22px;line-height:28px;color:var(--white)}
.hero-title .accent{color:var(--rose);font-size:20px}
.hero-note{left:318px;top:67px;width:118px;font-size:7px;line-height:9.5px;color:var(--white)}
.btn{display:flex;align-items:center;justify-content:center;background:var(--plum);color:var(--white);font-weight:700;border-radius:4px}
.hero-btn{left:318px;top:121px;width:68px;height:19px;font-size:7px}
/* info cards */
.card{background:var(--blush);border-radius:5px}
.ribbon{position:absolute;background:var(--plum);color:var(--white);font-family:"Open Sans",sans-serif;font-weight:700;display:flex;align-items:center;justify-content:center;border-left:4px solid var(--accent-blue);border-right:4px solid var(--accent-blue)}
.list{position:absolute;left:0;width:100%;text-align:center}
.list .label{font-weight:700;font-size:7.5px;color:var(--ink)}
.list .value{font-size:6.5px;color:var(--ink-soft);margin-top:6px}
.list .label.hl{color:var(--plum)}
.card-note{position:absolute;width:100%;text-align:center;color:var(--plum);font-weight:700;font-size:6.5px;line-height:9px}
/* mission */
.mission-title{left:71px;top:546px;font-family:"Open Sans",sans-serif;font-weight:700;font-size:11px;color:var(--plum)}
.mission-text{left:71px;top:571px;width:162px;font-size:7px;line-height:18.7px;color:var(--ink-soft)}
.brand-float{left:270px;top:560px;display:flex;align-items:center;gap:8px;font-family:"Source Sans 3",sans-serif;font-weight:700;font-size:26px;color:#e98bb0}
.brand-float .circle{width:22px;height:22px;border-radius:50%;background:#e98bb0}
/* services grid */
.tile{position:absolute;width:138px;height:125px}
.tile-white{background:var(--white);text-align:center}
.tile-plum{background:var(--plum);color:var(--white);text-align:center}
.photo{position:absolute;width:138px;height:125px}
.tile-label{position:absolute;left:0;width:100%;font-family:"Open Sans",sans-serif;font-weight:700;font-size:10.5px;color:var(--plum)}
.tile-plum .tile-label{color:var(--white)}
.tile-text{position:absolute;left:22px;width:94px;font-size:6.5px;line-height:11.5px}
.tile-btn{position:absolute;left:46px;width:52px;height:15px;background:var(--white);color:var(--plum);border-radius:4px;font-size:5.5px;font-weight:700;display:flex;align-items:center;justify-content:center}
.notch-down{position:absolute;width:0;height:0;border-left:11px solid transparent;border-right:11px solid transparent;border-top:11px solid var(--white)}
.notch-up{position:absolute;width:0;height:0;border-left:14px solid transparent;border-right:14px solid transparent;border-bottom:14px solid var(--plum)}
/* features */
.feature{position:absolute;top:959px;width:183.5px;height:167px;background:var(--white);text-align:center}
.feature.alt{background:var(--blush-soft)}
.feature .icon{position:absolute;left:76px;top:20px}
.feature h3{position:absolute;left:0;width:100%;top:63px;font-family:"Open Sans",sans-serif;font-weight:700;font-size:11px;line-height:15.5px;color:var(--plum)}
.feature p{position:absolute;left:22px;width:140px;font-size:7px;line-height:9.5px;color:var(--ink-soft)}
.feature .corner{position:absolute;right:0;bottom:0;width:0;height:0;border-left:31px solid transparent;border-bottom:26px solid var(--plum)}
/* booking */
.booking{left:101px;top:1159px;width:339px;height:194px}
.field{position:absolute;background:var(--white);border-radius:5px;font-size:6.5px;color:#8a8087;padding-left:9px;display:flex;align-items:center}
.submit{left:237px;top:1328px;width:68px;height:19px;font-size:7.5px;position:absolute}
/* footer */
.footer-tagline{left:0;width:565px;top:1460px;text-align:center;color:var(--white);font-weight:700;font-size:10px}
.footer-brand{left:0;width:565px;top:1427px;text-align:center;color:var(--white);font-weight:700;font-size:11px}
.help{left:0;width:551px;text-align:center;top:1492px;font-weight:700;font-size:7px;color:var(--ink)}
.phone{left:0;width:555px;text-align:center;top:1502px;font-weight:700;font-size:15px;color:var(--ink)}
.address{left:0;width:555px;text-align:center;top:1578px;font-weight:700;font-size:7px;line-height:11px;color:var(--white)}
.email{left:0;width:555px;text-align:center;top:1605px;font-weight:700;font-size:7px;color:var(--plum-dark)}
.map{left:0;top:1635px;width:551px;height:170px}
.footbar{left:0;top:1805px;width:551px;height:58px;background:var(--plum);color:var(--white);font-size:6.5px}
.footlinks{position:absolute;text-align:center;line-height:9.3px}
.social{position:absolute;width:13px;height:13px;border:1.5px solid var(--white);border-radius:3px}
</style>
</head>
<body>
<div class="stage">
<main class="page">

  <!-- HERO -->
  <svg class="hero-shape" width="551" height="230" viewBox="0 0 551 230" role="img" aria-label="Photo of a guest relaxing in an infrared sauna">
    <defs>
      <linearGradient id="heroTone" x1="0" y1="0" x2="1" y2="1">
        <stop offset="0" stop-color="#2f2230"/>
        <stop offset=".5" stop-color="#5a3f52"/>
        <stop offset="1" stop-color="#3b2a38"/>
      </linearGradient>
    </defs>
    <polygon points="0,0 551,0 551,156 274,228 0,156" fill="url(#heroTone)"/>
  </svg>
  <div class="abs brand-mark"><span class="dot"></span>EBBTIDE HAVEN</div>
  <nav class="abs nav" style="left:0;width:551px">
    <a class="is-active" style="left:192px">Home</a>
    <a style="left:238px">Float</a>
    <a style="left:282px">IR Sauna</a>
    <a style="left:341px">mHBOT</a>
    <a style="left:395px">Biomat</a>
    <a style="left:448px">Gift cards</a>
    <a style="left:509px;font-weight:700">Login</a>
  </nav>
  <h1 class="abs hero-title"><span class="accent">EBBTIDE</span><br>HAVEN.<br>SPA.</h1>
  <p class="abs hero-note">Click on the booking above if you know exactly what you want, otherwise feel free to browse below for more info.</p>
  <div class="abs btn hero-btn">BOOK NOW</div>

  <!-- PRICING -->
  <section class="abs card" style="left:72px;top:185px;width:171px;height:323px">
    <div class="ribbon" style="left:-14px;top:28px;width:194px;height:26px;font-size:16px;transform:rotate(12deg)">Pricing</div>
    <div class="list" style="top:74px"><div class="label">60 min Float Tenk</div><div class="value">$65.00</div></div>
    <div class="list" style="top:120px"><div class="label">30 min IR Sauna</div><div class="value">$40.00</div></div>
    <div class="list" style="top:166px"><div class="label">45 min BioMat</div><div class="value">$45.00</div></div>
    <div class="list" style="top:212px"><div class="label">60 min mHBOT</div><div class="value">$70.00</div></div>
    <div class="list" style="top:258px"><div class="label hl">Membership*</div><div class="value">$25.00 per month</div></div>
    <div class="card-note" style="top:305px">$20.00 off every booking!</div>
  </section>

  <!-- HOURS -->
  <section class="abs card" style="left:311px;top:242px;width:171px;height:238px">
    <div class="ribbon" style="left:-14px;top:25px;width:194px;height:26px;font-size:16px;transform:rotate(12deg)">Hours</div>
    <div class="list" style="top:73px"><div class="label">Early session</div><div class="value">6am-9am</div></div>
    <div class="list" style="top:118px"><div class="label">Normal session</div><div class="value">9am-5pm</div></div>
    <div class="list" style="top:164px"><div class="label">Late session</div><div class="value">5pm-10pm</div></div>
    <div class="card-note" style="top:211px;left:25px;width:121px">We open earlier and stay open longer,just for you.</div>
  </section>

  <!-- MISSION -->
  <div class="abs brand-float"><span class="circle"></span>Ebbtide Haven</div>
  <h2 class="abs mission-title">OUR MISSION</h2>
  <p class="abs mission-text">Our mission is to provide a purpose-built space for our clients to relax,recover and optimise their health. Ebbtide Haven offers Flotation Therapy,Mild Hyperbaric Oxygen Therapy (mHBOT), Infrared Saun and Biomat sessions.</p>

  <!-- SERVICES -->
  <div class="tile tile-white" style="left:0;top:710px">
    <svg class="abs" style="left:44px;top:32px" width="50" height="38" viewBox="0 0 50 38" aria-hidden="true">
      <defs><linearGradient id="iconGrad" x1="0" y1="0" x2="1" y2="1"><stop offset="0" stop-color="#e07aa6"/><stop offset="1" stop-color="#4fb9bf"/></linearGradient></defs>
      <path d="M4 22 C10 6 30 6 34 18 C30 30 12 32 4 22 Z" fill="none" stroke="url(#iconGrad)" stroke-width="2.5"/>
      <path d="M2 32 C14 26 30 38 46 30" fill="none" stroke="url(#iconGrad)" stroke-width="2.5"/>
    </svg>
    <div class="tile-label" style="top:88px">FLOAT</div>
  </div>
  <div class="photo" style="left:137.5px;top:710px;background:linear-gradient(135deg,#c8956a,#8e6248)" role="img" aria-label="Photo of a man resting in a wooden infrared sauna"></div>
  <div class="tile tile-white" style="left:275px;top:710px">
    <div class="abs" style="left:0;width:100%;top:26px;font-family:'Open Sans',sans-serif;font-weight:800;font-size:34px;color:#b0568c">O<sup style="font-size:16px;color:#e0607f">2</sup></div>
    <div class="tile-label" style="top:89px">mHBOT</div>
  </div>
  <div class="photo" style="left:412.5px;top:710px;background:linear-gradient(135deg,#f2f0f0,#d8cfcb)" role="img" aria-label="Photo of a heated biomat on a white background"></div>

  <div class="photo" style="left:0;top:834px;background:radial-gradient(circle at 50% 55%,#c8b8e8,#9e86cf 60%,#e6e0f0)" role="img" aria-label="Photo of a woman floating in a float pod"></div>
  <div class="notch-down" style="left:58px;top:834px"></div>
  <div class="tile tile-plum" style="left:137.5px;top:834px">
    <div class="tile-label" style="top:16px">IR SAUNA</div>
    <div class="tile-text" style="top:35px">Turbocharge your detox with our Infrared sauna.</div>
    <div class="tile-btn" style="top:92px">BOOK NOW</div>
  </div>
  <div class="notch-up" style="left:193px;top:821px"></div>
  <div class="photo" style="left:275px;top:834px;background:linear-gradient(135deg,#2f8fd8,#0f4a8c 70%,#b8c6d8)" role="img" aria-label="Photo of a woman lying in a hyperbaric oxygen chamber"></div>
  <div class="notch-down" style="left:333px;top:834px"></div>
  <div class="tile tile-plum" style="left:412.5px;top:834px">
    <div class="tile-label" style="top:20px">BIOMAT</div>
    <div class="tile-text" style="top:44px">Relax,recharge and replenish. Simple.</div>
    <div class="tile-btn" style="top:92px">BOOK NOW</div>
  </div>
  <div class="notch-up" style="left:462px;top:821px"></div>

  <!-- FEATURES -->
  <div class="feature" style="left:0">
    <svg class="icon" width="32" height="32" viewBox="0 0 32 32" aria-hidden="true">
      <circle cx="16" cy="16" r="13" fill="none" stroke="#c9a13a" stroke-width="3"/>
      <path d="M16 9 V16 L22 20" fill="none" stroke="#7a5a80" stroke-width="2.5" stroke-linecap="round"/>
    </svg>
    <h3>HOURS SERVICE</h3>
    <p style="top:103px">We open earlier and stay open longer, just for you.</p>
    <span class="corner"></span>
  </div>
  <div class="feature alt" style="left:183.5px">
    <svg class="icon" width="32" height="32" viewBox="0 0 32 32" aria-hidden="true">
      <circle cx="16" cy="9" r="6" fill="none" stroke="#c9a13a" stroke-width="3"/>
      <path d="M5 29 V24 C5 19 27 19 27 24 V29 Z" fill="none" stroke="#4fa7b8" stroke-width="3"/>
    </svg>
    <h3>PROFESSIONAL<br>EMPLOYEES</h3>
    <p style="top:105px">Workers with extensive experience in a certain field.</p>
    <span class="corner"></span>
  </div>
  <div class="feature" style="left:367px">
    <svg class="icon" width="32" height="32" viewBox="0 0 32 32" aria-hidden="true">
      <polygon points="16,2 20,12 31,12 22,19 25,30 16,23 7,30 10,19 1,12 12,12" fill="none" stroke="#7a5a80" stroke-width="3" stroke-linejoin="round"/>
    </svg>
    <h3>MODERN EQUIPMENT</h3>
    <p style="top:105px">We offer superior,quality and new equiment.</p>
    <span class="corner"></span>
  </div>

  <!-- QUICK BOOKING -->
  <section class="abs card booking">
    <div class="ribbon" style="left:-12px;top:11px;width:363px;height:22px;font-size:13px;transform:rotate(2.5deg)">Quick booking</div>
    <div class="field" style="left:14px;top:55px;width:152px;height:15px">Name*</div>
    <div class="field" style="left:173px;top:55px;width:152px;height:15px">Email address*</div>
    <div class="field" style="left:14px;top:76px;width:152px;height:15px">Phone number*</div>
    <div class="field" style="left:173px;top:76px;width:152px;height:15px">How did you hear about us?*</div>
    <div class="field" style="left:14px;top:97px;width:311px;height:65px"></div>
  </section>
  <div class="btn submit">SUBMIT</div>

  <!-- FOOTER -->
  <svg class="abs" style="left:0;top:1385px" width="551" height="250" viewBox="0 0 551 250" aria-hidden="true">
    <defs>
      <radialGradient id="footGlow" cx="50%" cy="52%" r="35%">
        <stop offset="0" stop-color="#e79ac8"/>
        <stop offset="1" stop-color="#a0578a"/>
      </radialGradient>
    </defs>
    <polygon points="0,72 279,0 551,72 551,250 0,250" fill="url(#footGlow)"/>
  </svg>
  <div class="abs footer-brand">EBBTIDE HAVEN</div>
  <div class="abs footer-tagline">Relax, recover and optimise your health</div>
  <div class="abs help">NEED HELP? CALL US</div>
  <div class="abs phone">1800 555 019</div>
  <svg class="abs" style="left:264px;top:1540px" width="26" height="32" viewBox="0 0 26 32" aria-hidden="true">
    <path d="M13 31 C13 31 1 19 1 12 A12 12 0 0 1 25 12 C25 19 13 31 13 31 Z" fill="#4a3f47"/>
    <circle cx="13" cy="12" r="4.5" fill="#c27aa8"/>
  </svg>
  <div class="abs address">Unit 4, 118 Marrow Road<br>Kelsworth, QLD, 4510</div>
  <div class="abs email">admin@ebbtidehaven.com.au</div>
  <div class="abs map" style="background:linear-gradient(120deg,#eceef0,#e3e6ea 60%,#dcebd8)" role="img" aria-label="Street map showing the spa location"></div>

  <footer class="abs footbar">
    <div class="footlinks" style="left:20px;width:100px;top:10px">Booking Policy<br>Membership Policy<br>Privacy Policy<br>Cancellation Policy</div>
    <div class="footlinks" style="left:235px;width:80px;top:20px">FAQs<br>Sitemap</div>
    <div class="footlinks" style="left:455px;width:60px;top:14px;font-weight:700">Follow US</div>
    <span class="social" style="left:466px;top:26px"></span>
    <span class="social" style="left:488px;top:26px;background:var(--white)"></span>
  </footer>

</main>
</div>
</body>
</html>
```